Web design for facial expression recognition service

We offer a service which allows customers to film large panels of participants looking at some video/screen (e.g. an advertisement) and to analyze the facial expressions shown by the participants. We are looking for the design of a new website which will make it easy for our customers to setup and view the results of these experiments online.
Competitor's websites that may serve as a reference are:
http://www.moravelt.example/pindor/#pane_overview
http://www.quintabrook.example/homepage.aspx
https://www.tavorlin.example/
The website will (for as far as the design is concerned) consist of three parts:
- A public home page (and perhaps some contact/news/about page), designed to catch the attention/interest potential customers.
- A (protected) project result page, showing the results in an interactive page with charts and numerical data.
- Pages (also protected) with fields and tables (setting up the project details).
The winner of this design project should provide us with at least one design for each of the above in order to get a complete 'theme' going which our developers can use. However, you are welcome to initially only provide the design for the project result page and/or home page.
We are looking for a modern, fresh, yet professional look (my client is a more established party in the field).
The final delivery should consist of layered Photoshop or Illustrator files.
Thank you in advance for participating!
Dear designers,
Reason: Extending the deadline by a few days to give designers a chance to submit designs for the other pages and process further feedback.
Target Market(s)
marketing research agencies (B2B service)
Industry/Entity Type
Delivery
Requirements
Must have
- Home page:
- Basic advertisement of the service; some quick explanation of how it works
- A way to login for existing users
- A link/button/banner inviting people to sign up
- Navigation controls to 2-3 other pages
- Social media links (Chatterbay, WorkNest group)
- Company logo (sorry, can't provide it as my client wishes to remain anonymous for now, but it's rounded and has blue as it's main color).
- Copyright / creator details
Project result page:
(see attachment 1 for a functional mockup - the design may follow this layout closely, or be completely different)
- Title
- A video player and basic numerical data
- Different views of the analysis results can dynamically be added/removed/collapsed/expanded; each one of these views will show some kind of chart, filters (combos), numerical data and a download button/link.
- A way to sign out, go to the main project page and go to the main page
- Logo
- Copyright
The form pages:
(see attachment 2 for a functional mockup of one of the pages; feel free to change some elements to better show the overall style)
- Title
- Text fields, combos, calendar pickers, tables, navigation links
- Logo
- Copyright
Nice to have
- Any creative text elements or product logo/symbol are a bonus. However, the basic "Lorem Ipsum" would do too.

```html
<!DOCTYPE html>
<html lang="en">
<head>
<meta charset="utf-8">
<title>Veldmoor — Facial Expression Analysis</title>
<link rel="stylesheet" href="https://fonts.googleapis.com/css2?family=Ubuntu:wght@400;500&family=PT+Sans:wght@400;700&display=swap">
<style>
:root{
  --ink:#333;
  --muted:#666;
  --soft:#888;
  --line:#dedede;
  --nav:#050505;
  --nav-text:#cfcfcf;
  --white:#fff;
  --field:#f3f3f3;
  --footer:#3b3b3b;
  --footer-text:#d6d6d6;
  --logo-dot:#9a9a9a;
}
*{box-sizing:border-box;margin:0;padding:0}
html,body{width:1111px;height:1200px;overflow:hidden;background:var(--white)}
body{position:relative;font-family:"PT Sans",Arial,sans-serif;color:var(--ink)}
.abs{position:absolute}
.line{display:block;white-space:nowrap}
.top-rule{left:0;top:0;width:1111px;height:5px;background:#333}

.brand{left:106px;top:14px;display:flex;align-items:center;gap:8px}
.brand-dot{width:49px;height:49px;border-radius:50%;background:var(--logo-dot)}
.brand-name{font-family:"Ubuntu",sans-serif;font-size:28px;font-weight:500;color:#6b6b6b}

.main-nav{left:437px;top:35px;width:575px;height:34px;background:var(--nav);border-radius:5px;
  display:flex;align-items:center;justify-content:space-around;padding:0 8px}
.main-nav a{font-family:"Ubuntu",sans-serif;font-size:16px;color:var(--nav-text);text-decoration:none}
.main-nav a.current{color:var(--white)}

.hero{left:92px;top:70px;width:927px;height:385px;
  background:radial-gradient(ellipse at 50% 45%,#e9c3a4 0%,#c99a78 35%,#6e5444 70%,#2f2a28 100%)}
.slider-dots{left:496px;top:426px;width:98px;height:34px;border-radius:8px;background:#8d8d8d;
  display:flex;align-items:center;justify-content:center;gap:11px}
.slider-dots i{width:9px;height:9px;border-radius:50%;background:#eee;display:block}

.step{width:250px;height:250px;border-radius:50%;background:radial-gradient(circle,#fff 70%,#f1f1f1 100%);
  box-shadow:0 0 6px rgba(0,0,0,.05);text-align:center}
.step h2{font-family:"Ubuntu",sans-serif;font-weight:400;font-size:23px;color:#444;margin-top:28px}
.step p{font-size:10.2px;line-height:18.5px;color:#444;margin:26px auto 0;width:240px}
.step .icon{width:62px;height:62px;margin:20px auto 0;border-radius:8px}

.section-title{font-family:"Ubuntu",sans-serif;font-weight:400;font-size:21px;color:#2e2e2e}

.video-thumb{left:127px;top:790px;width:296px;height:201px;border-radius:4px;
  background:linear-gradient(160deg,#dfe6ee 0%,#c9d7e6 40%,#e7d2c2 70%,#b9c2cc 100%)}
.play{left:251px;top:853px;width:52px;height:52px}
.video-caption{left:129px;top:998px;font-size:15px;color:#444;white-space:nowrap}
.video-text{left:129px;top:1026px;width:300px;font-size:12.5px;line-height:21px;color:#777}

.login-head{left:463px;top:745px;display:flex;align-items:center;gap:12px}
.panel{background:var(--white);border:1px solid #e3e3e3;border-radius:4px;box-shadow:0 2px 4px rgba(0,0,0,.06)}
.login-box{left:446px;top:796px;width:274px;height:139px}
.field{position:absolute;left:17px;width:244px;height:25px;background:var(--field);border:1px solid #cfcfcf;
  font-family:Arial,sans-serif;font-size:10px;color:#555;padding:6px 13px}
.btn{position:absolute;background:linear-gradient(#3a3a3a,#000);color:var(--white);border-radius:14px;
  font-family:"PT Sans",Arial,sans-serif;font-weight:700;text-align:center;box-shadow:0 1px 2px rgba(0,0,0,.4)}
.submit{left:173px;top:101px;width:89px;height:25px;font-size:13.5px;line-height:25px;letter-spacing:.5px}

.signup-box{left:446px;top:945px;width:274px;height:139px;overflow:hidden}
.signup-kicker{position:absolute;left:21px;top:17px;font-family:"Ubuntu",sans-serif;font-size:13px;color:#333}
.signup-title{position:absolute;left:21px;top:32px;font-family:"Ubuntu",sans-serif;font-size:19px;color:#333}
.signup-text{position:absolute;left:21px;top:60px;width:115px;font-size:10.5px;line-height:16px;color:#999}
.signup-btn{left:19px;top:94px;width:68px;height:25px;font-size:11.5px;line-height:25px}
.signup-photo{position:absolute;left:140px;top:4px;width:133px;height:135px;
  background:linear-gradient(180deg,#f3f3f3 0%,#e7d3c6 45%,#f5f5f5 100%)}

.testimonial-photo{left:744px;top:798px;width:87px;height:77px;border-radius:3px;
  background:radial-gradient(circle at 50% 45%,#e7a983,#b26b44 80%)}
.quote{font-size:12.5px;line-height:20.4px;color:#444}
.quote .line{text-align:justify;text-align-last:justify}
.quote .line.last{text-align-last:left}
.quote-a{left:847px;top:795px;width:152px}
.quote-b{left:746px;top:887px;width:253px}
.client{left:746px;top:980px;font-size:12.5px;line-height:20.4px;color:#333}
.read-more{left:931px;top:1030px;width:68px;height:25px;font-size:11.5px;line-height:25px;border-radius:12px}

.footer{left:0;top:1105px;width:1111px;height:95px;
  background:radial-gradient(ellipse 320px 120px at 410px 105px,#8a8a8a 0%,#4a4a4a 60%,var(--footer) 100%),var(--footer)}
.footer-nav{left:105px;top:1127px;font-family:Arial,sans-serif;font-size:11.5px;color:var(--footer-text);word-spacing:2px}
.footer-nav span{margin:0 6px}
.copyright{left:105px;top:1151px;font-family:Arial,sans-serif;font-size:11.5px;color:var(--footer-text)}
.social{left:860px;top:1136px;display:flex;gap:14px}
.social a{display:flex;align-items:center;gap:5px;font-family:Arial,sans-serif;font-size:11px;color:var(--footer-text);text-decoration:none}
.social a i{width:10px;height:10px;border-radius:50%;background:#7fb7d8;display:block}
</style>
</head>
<body>
<div class="abs top-rule"></div>

<header>
  <div class="abs brand"><span class="brand-dot"></span><span class="brand-name">Veldmoor</span></div>
  <nav class="abs main-nav">
    <a class="current" href="#">Home</a><a href="#">About Us</a><a href="#">Video</a>
    <a href="#">Services</a><a href="#">How it Works</a><a href="#">Contact</a>
  </nav>
</header>

<div class="abs hero" role="img" aria-label="Photo of a smiling group of people huddled together, several faces highlighted by square detection frames"></div>
<div class="abs slider-dots"><i></i><i></i><i></i><i></i></div>

<section>
  <div class="abs step" style="left:122px;top:479px">
    <h2>Step 1</h2>
    <p><span class="line">On the Internet. It uses a dictionary of over 200</span><span class="line">Latin words, combined with a handful of model</span><span class="line">sentence structures, to generate Lorem Ipsum</span></p>
    <div class="icon" role="img" aria-label="Magic hat illustration" style="background:radial-gradient(circle,#3a4a5a,#111 70%)"></div>
  </div>
  <div class="abs step" style="left:431px;top:479px">
    <h2>Step 2</h2>
    <p><span class="line">On the Internet. It uses a dictionary of over 200</span><span class="line">Latin words, combined with a handful of model</span><span class="line">sentence structures, to generate Lorem Ipsum</span></p>
    <div class="icon" role="img" aria-label="Film clapperboard illustration" style="background:linear-gradient(#333 0 22%,#2d8fc4 22%,#7cc6ee)"></div>
  </div>
  <div class="abs step" style="left:747px;top:479px">
    <h2>Step 3</h2>
    <p><span class="line">On the Internet. It uses a dictionary of over 200</span><span class="line">Latin words, combined with a handful of model</span><span class="line">sentence structures, to generate Lorem Ipsum</span></p>
    <div class="icon" role="img" aria-label="Laptop with globe illustration" style="background:radial-gradient(circle at 65% 35%,#5aa3e0,#1d2b3a 65%)"></div>
  </div>
</section>

<section>
  <h3 class="abs section-title" style="left:129px;top:752px">Watch Our Video</h3>
  <div class="abs video-thumb" role="img" aria-label="Photo of hands typing on a laptop with floating media thumbnails"></div>
  <svg class="abs play" viewBox="0 0 52 52" aria-hidden="true">
    <circle cx="26" cy="26" r="24" fill="rgba(90,90,90,.75)" stroke="#ddd" stroke-width="3"/>
    <path d="M20 15 L37 26 L20 37 Z" fill="#fff"/>
  </svg>
  <p class="abs video-caption">Phasellus felis dolor, scelerisque a, tempus</p>
  <p class="abs video-text"><span class="line">eget, lobortis id, libero. Donec scelerisque leo ac risus.</span><span class="line">Praesent sit amet est. In dictum</span></p>
</section>

<section>
  <div class="abs login-head">
    <svg width="32" height="40" viewBox="0 0 32 40" aria-hidden="true">
      <path d="M8 18 V11 a8 8 0 0 1 16 0 V18" fill="none" stroke="#8a8a8a" stroke-width="4"/>
      <rect x="3" y="17" width="26" height="21" rx="3" fill="#9a9a9a"/>
      <rect x="8" y="21" width="3" height="13" fill="#c8c8c8"/>
    </svg>
    <h3 class="section-title">Member Login</h3>
  </div>
  <form class="abs panel login-box">
    <div class="field" style="top:18px">Username</div>
    <div class="field" style="top:56px">Password</div>
    <div class="btn submit">SUBMIT</div>
  </form>
  <div class="abs panel signup-box">
    <div class="signup-kicker">Member Please</div>
    <div class="signup-title">Sign Up here</div>
    <p class="signup-text">Lorem ipsum dolor sit amet, consectetuer</p>
    <div class="btn signup-btn">SIGN UP</div>
    <div class="signup-photo" role="img" aria-label="Photo of a smiling woman giving two thumbs up"></div>
  </div>
</section>

<section>
  <h3 class="abs section-title" style="left:749px;top:755px">Testimonials</h3>
  <div class="abs testimonial-photo" role="img" aria-label="Portrait photo of the client"></div>
  <p class="abs quote quote-a">
    <span class="line">"The Internet. It uses a</span>
    <span class="line">dictionary of over 200 Latin</span>
    <span class="line">words, combined with a</span>
    <span class="line">handful of model sentence</span>
  </p>
  <p class="abs quote quote-b">
    <span class="line">Consectetur, adipisci velit, sed quia non</span>
    <span class="line">numquam eius modi tempora incidunt ut</span>
    <span class="line">labore etlarn dolore magnam aliquam quaerat</span>
    <span class="line last">voluptatem. "</span>
  </p>
  <p class="abs client">Client Name<br>City</p>
  <div class="abs btn read-more">Read More</div>
</section>

<footer>
  <div class="abs footer"></div>
  <nav class="abs footer-nav">Home<span>-</span>About<span>-</span>Products<span>-</span>Blog<span>-</span>Contact<span>-</span>Register<span>-</span>Login</nav>
  <p class="abs copyright">Copyright &nbsp;©&nbsp; 2013 &nbsp;www.veldmoor.example &nbsp;&nbsp; All rights reserved.</p>
  <div class="abs social">
    <a href="#"><i></i>Chatterbay</a>
    <a href="#"><i></i>Chirplane</a>
    <a href="#"><i></i>WorkNest</a>
  </div>
</footer>
</body>
</html>
```